Logo and Business card design!

Welbrook Estates

We are a Property development and real estate company (needs a logo design).

Welbrook estates is based in Sydney Australia and will be dealing with high net worth individuals with a corporate background. The demographic of clients will be relatively youthful and savvy. We do development finance, property development and some portion of property sales

I'd like the 'Welbrook' part of the name to be strength of the title, with 'property' playing a very minor part, perhaps in tiny font somewhere off to the bottom or side or something

Thank you!

Target Market(s)

25-55 years old

Industry/Entity Type

Real Estate Development

Contact Information for Business Card

Please arrange this information as you see fit

Leon Brightwater
Managing Director
0417 582 273
leon@welbrookestates-example.com.au
www.welbrookestates-example.com.au

Logo Text

Welbrook estates

Font styles to use
Serif

Colors

Designer to choose colors to be used in the design.

Requirements
Must have
• PLEASE VIEW THE UPLOADED IMAGES AND EXAMPLES
• And please put 'property' in small letters at the bottom or to the side. I want it to play a minimalist role, with 'WELBROOK' being the feature
• Colours! Please make sure theyre mostly grey and white with possibly some other dark blue and maybe dark grey
Nice to have
• Please feel free to use whatever colors you like, the suggested colors are something I selected momentarily and dont necessarily reflect strict guidelines
Should not have
• NO pictures or shapes of houses. I dont want the logo design to be so literal in its imagery

```html
<!DOCTYPE html>
<html lang="en">
<head>
<meta charset="utf-8">
<title>Welbrook Estates — Business Card</title>
<link rel="stylesheet" href="https://fonts.googleapis.com/css2?family=Montserrat:wght@500;600;700&display=swap">
<style>
  :root {
    --navy: #272262;
    --white: #ffffff;
    --ink: #333333;
    --page: #ffffff;
  }
  * { margin: 0; padding: 0; box-sizing: border-box; }
  html, body {
    width: 1200px;
    height: 355px;
    overflow: hidden;
    background: var(--page);
    font-family: "Montserrat", Arial, sans-serif;
  }
  .canvas {
    position: relative;
    width: 1200px;
    height: 355px;
    background: var(--page);
  }
  .card-back {
    position: absolute;
    left: 0; top: 0;
    width: 562px; height: 355px;
    background: var(--navy);
  }
  .card-front-band {
    position: absolute;
    left: 625px; top: 0;
    width: 575px; height: 232px;
    background: var(--navy);
  }
  .wordmark {
    position: absolute;
    transform: translate(-50%, -50%);
    color: var(--white);
    font-weight: 600;
    text-align: center;
    line-height: 1;
    white-space: nowrap;
  }
  .wordmark .name { display: block; letter-spacing: 0.02em; }
  .wordmark .sub { display: block; letter-spacing: 0.32em; margin-top: 10px; }
  .wordmark--back { left: 281px; top: 172px; }
  .wordmark--back .name { font-size: 42px; }
  .wordmark--back .sub { font-size: 13px; }
  .wordmark--front { left: 905px; top: 116px; }
  .wordmark--front .name { font-size: 38px; }
  .wordmark--front .sub { font-size: 12px; }

  .person {
    position: absolute;
    left: 640px; top: 273px;
    color: var(--ink);
  }
  .person__name { font-size: 21px; font-weight: 600; line-height: 1; }
  .person__title { font-size: 12.5px; font-weight: 700; margin-top: 9px; line-height: 1; }

  .divider {
    position: absolute;
    left: 860px; top: 250px;
    width: 2px; height: 92px;
    background: var(--ink);
  }
  .contacts {
    position: absolute;
    left: 881px; top: 263px;
    list-style: none;
  }
  .contacts li {
    display: flex;
    align-items: center;
    height: 22.5px;
    color: var(--ink);
    font-size: 13px;
    font-weight: 600;
    white-space: nowrap;
  }
  .contacts svg { width: 16px; height: 16px; margin-right: 9px; flex: none; }
</style>
</head>
<body>
<main class="canvas">
  <section class="card-back">
    <div class="wordmark wordmark--back">
      <span class="name">WELBROOK</span>
      <span class="sub">ESTATES</span>
    </div>
  </section>

  <section class="card-front-band">
  </section>
  <div class="wordmark wordmark--front">
    <span class="name">WELBROOK</span>
    <span class="sub">ESTATES</span>
  </div>

  <div class="person">
    <p class="person__name">Leon Brightwater</p>
    <p class="person__title">Managing Director</p>
  </div>

  <div class="divider"></div>

  <ul class="contacts">
    <li>
      <svg viewBox="0 0 16 16" aria-hidden="true">
        <circle cx="8" cy="8" r="8" fill="#333333"/>
        <path d="M5.4 4.2l1.3-.3.8 2-1 .7c.5 1.1 1.3 1.9 2.4 2.4l.7-1 2 .8-.3 1.3c-.2.6-.8.9-1.4.8C7.5 10.4 5.6 8.5 5 6.1c-.1-.6.2-1.2.4-1.9z" fill="#ffffff"/>
      </svg>
      0417 582 273
    </li>
    <li>
      <svg viewBox="0 0 16 16" aria-hidden="true">
        <circle cx="8" cy="8" r="8" fill="#333333"/>
        <text x="8" y="11.3" text-anchor="middle" font-family="Montserrat, Arial, sans-serif" font-size="10" font-weight="700" fill="#ffffff">@</text>
      </svg>
      leon@welbrookestates-example.com.au
    </li>
    <li>
      <svg viewBox="0 0 16 16" aria-hidden="true">
        <circle cx="8" cy="8" r="8" fill="#333333"/>
        <g fill="none" stroke="#ffffff" stroke-width="0.9">
          <circle cx="8" cy="8" r="4.6"/>
          <ellipse cx="8" cy="8" rx="2" ry="4.6"/>
          <line x1="3.4" y1="8" x2="12.6" y2="8"/>
        </g>
      </svg>
      www.welbrookestates-example.com.au
    </li>
  </ul>
</main>
</body>
</html>
```